Meatball Posters

We are opening a Meatball Sandwich Shop called
Harlow's Famous Meatball Kitchen. It is a quirky concept with a fun, casual, and sometime mildly inappropriate theme.
Sandwiches Like
"Pink Pickle" Blue Cheese Bacon Meatball Sandwich
"Chiflado" Tex Mex Meatball Sandwich
"Big Trouble Tonight" Classic Meatball Sandwich
You get the idea......We are covering the interior of the place with posters of different meatball things.....That is where this comes in. I am looking for fun, quirky posters that incorporate meatballs. Think along the lines of the movie "Windy Weeks Full of Flying Dumplings.....Think of a posted of the last supper with a giant cartoon bowl of meatballs on the table....nothing is off the table. We just need our customers to look at it and chuckle, laugh or think...
It is a fast food type place and the logo is red and yellow. I uploaded a color scheme but don't feel you are limited to just that. It is just a guide.
Target Market(s)
Blue collar workers, college kids,
Industry/Entity Type
Movie
Requirements
Must have
- It has to be fun and quirky but not too offensive or inappropriate
Nice to have
- Look at the color scheme I uploaded...I like the idea of doing it cartoon "like"
Should not have
- No Porn....abusive etc...

```html
<!DOCTYPE html>
<html lang="en">
<head>
<meta charset="utf-8">
<title>I Love Meatballs Poster</title>
<link rel="stylesheet" href="https://fonts.googleapis.com/css2?family=Nunito:wght@900&display=swap">
<style>
  :root {
    --poster-red: #bd1e2e;
    --type-white: #ffffff;
    --meatball-light: #e8a070;
    --meatball-mid: #d4825a;
    --meatball-dark: #a8623c;
  }
  html, body {
    margin: 0;
    padding: 0;
    width: 800px;
    height: 1200px;
    overflow: hidden;
    background: var(--poster-red);
  }
  .poster {
    position: relative;
    width: 800px;
    height: 1200px;
    background: var(--poster-red);
    font-family: "Nunito", sans-serif;
    color: var(--type-white);
  }
  .headline {
    margin: 0;
    font-weight: 900;
  }
  .headline-i {
    position: absolute;
    left: 268px;
    top: 355px;
    font-size: 152px;
    line-height: 1;
  }
  .meatball-heart {
    position: absolute;
    left: 341px;
    top: 347px;
    width: 179px;
    height: 146px;
  }
  .headline-word {
    position: absolute;
    left: 0;
    width: 800px;
    top: 492px;
    text-align: center;
    font-size: 165px;
    line-height: 1;
    letter-spacing: -6px;
    transform: scaleX(0.89);
    transform-origin: 400px 0;
  }
</style>
</head>
<body>
  <main class="poster">
    <h1 class="headline">
      <span class="headline-i">I</span>
      <svg class="meatball-heart" viewBox="0 0 179 146" role="img" aria-label="Cartoon meatball shaped like a heart, meaning love">
        <defs>
          <radialGradient id="meatball-tone" cx="40%" cy="35%" r="70%">
            <stop offset="0%" stop-color="var(--meatball-light)"/>
            <stop offset="60%" stop-color="var(--meatball-mid)"/>
            <stop offset="100%" stop-color="var(--meatball-dark)"/>
          </radialGradient>
        </defs>
        <path fill="url(#meatball-tone)" d="M89 30 C80 8 60 2 40 4 C14 8 2 28 4 52 C7 82 40 104 62 122 C74 132 82 140 89 144 C96 140 104 132 116 122 C138 104 172 82 175 52 C177 28 165 8 139 4 C119 2 98 8 89 30 Z"/>
      </svg>
      <span class="headline-word">Meatballs</span>
    </h1>
  </main>
</body>
</html>
```